Norwegian psychologist service needs a fresh and exiting web site*

Norwegian psychologist service: working with therapy, personal development, mastery and personal growth. Focus: children and teenagers with special needs; family dynamics; group processes; individuals with a need for therapy and personal growth. (Our company name: Fjordlys og samhold (means Mastery and Growth).

We already have a logo for the company, which will be used (will be attached in the project).

The webside is to be structured in 4 pages with roll down curtain menus (the numbers are just for guiding the designer - the should not be added):

Page 1: Om Fjordlys og Samhold (about Mastery and Growth): this is where our business is is presented/described shortly: Lorem Ipsum dolor cit...

Page 2: Tjenester (Services): this is where our 5 service areas are presented:
2.1 Utredning (Investigation, diagnosing): Lorem Ipsum dolor cit...
2.2 Rådgivning (consulting): Lorem Ipsum dolor cit...

2.3 Kurs og work shops (courses and work shops): Lorem Ipsum dolor cit...
2.3a Fjordlys og samhold Tema 1 (T1)
2.3b Fjordlys og samhold Tema 2 (T2)
2.3c Fjordlys og samhold Tema 3 (T3)

2.4 Terapi og utvikling (Therapy and development)
2.4a Fjordlys og samhold for individer (FS1)
2.4b Fjordlys og samhold i familier (FS2)
2.4c Fjordlys og samhold i grupper (FS3)
2.4d Fjordlys og samhold i institusjoner (FS4)

Page 3: Aktuelt (Blog): this is our blog where we share knowledge and articles

Page 4: Kontakt (Contact): This is the contact form page. Contact form should constitute:
- Ditt navn (your name)
- E-post (your e-mail)
- Emne (subject)
- Melding (message/description)

Our project should also include suggestion for handheld units (iPhone, iPad).
Updates

We have both been traveling with work for a while, and then unfortunately both of us got sick on return, so we need a few more days to evaluate and choose design. Kind Regards Arvid & Margit

Target Market(s)

Focus on therapy, learning, mastery and growth for children and teenagers with special needs, within the family dynamics, or in a group setting.
OUR MARKETS:
Private market: individuals, families, groups and health industry institutions (with focus on learning, mastery, growth (as well as growing up) and psychiatry for children and teenagers with special difficulties and needs)
Public institutions: Government institutions, state institutions and municipality institutions (e.g. schools, municipality health service, hospitals) that serve the public (families with children and teenagers with special needs, and where learning, mastery, growth (as well as growing up) and potential psychiatry is an issue).

Number of Pages Required

4 page

Font styles to use
Sans Serif

Colors

Designer to choose colors to be used in the design.

Requirements
Must have
• The website must have 4 pages with roll down curtain menus (we have added a PDF with suggested structure, and headings, with sub menus - see attached PDF drawing.
• The web page must also use the added logo file - and make the web page work well with our logo.
• We would like the website to have a modern look and we would like the site to be associated with typical HIGH END TOP QUALITY private health institutions, but with a stronger focus on human beings (hands, faces etc), and not white coats and doctors. We are psychologists in the private market.
• For instance, if photos are being used - we tend to like "warm" almost art-like, "grainy" two-tone (e.g. sepia) photos to illustrate our focus. If designer can find such photos as part of design, it would be interesting to us. We would like a few photos like that integrated in the design.
• We also want a design suggestion for how the web page should look like and behave on handheld units (e.g. iPhone, iPad).
Nice to have
• If designer could find a number of suitable photos that matches the business idea and design requirements (see description above), that could follow website, that would be good.
• It could also be nice to have graphic symbols that denote the different pages/subpages (subjects)....
• HORSES: we sometimes use horses as a "tool" in therapy sessions. The horse is not necessarily used for riding, but for contact, communication and grooming. PHOTOS: we would like the designer to find an opportunity for using a photo reflecting this cooperation between therapist, child, teenager and horse. It is a bit up to the designer to find a way to do this... Since the horse is only a tool, among many other tools, it does not have to be much - but we want to try and see how it will work with a photo that also reflects this part of our business.

```html
<!DOCTYPE html>
<html lang="en">
<head>
<meta charset="utf-8">
<title>Fjordlys og samhold</title>
<link href="https://fonts.googleapis.com/css2?family=Montserrat:wght@400;500;600;700;800&display=swap" rel="stylesheet">
<style>
:root{
  --pink:#c9617f;
  --pink-soft:#e5b0c0;
  --teal:#63b7ad;
  --ink:#2f2f2f;
  --text:#333;
  --white:#fff;
}
*{margin:0;padding:0;box-sizing:border-box}
html,body{width:738px;height:1200px;overflow:hidden;background:var(--white)}
body{font-family:'Montserrat',sans-serif;color:var(--text);position:relative}
.abs{position:absolute}
.nav-links{position:absolute;top:11px;right:79px;display:flex;gap:15px;font-size:6.4px;font-weight:500;letter-spacing:.2px;color:var(--ink);list-style:none}
.brand{position:absolute;left:70px;top:9px;display:flex;align-items:center;gap:4px;font-size:7px;font-weight:600;color:#2c3a7a}
.brand-dot{width:10px;height:10px;border-radius:50%;background:#2c3a7a}
.hero-photo{position:absolute;left:0;top:0;width:738px;height:246px;
  background:linear-gradient(180deg,rgba(255,255,255,.95) 0%,rgba(255,255,255,0) 30%),
  linear-gradient(90deg,#6c4a4f 0%,#b58a92 35%,#f3e6e4 62%,#c98a7d 78%,#7a5a4a 100%)}
.hero-panel{position:absolute;left:0;top:49px;width:407px;height:131px;background:rgba(229,176,192,.97);border-radius:0 34px 34px 0}
.hero-title{position:absolute;left:79px;top:64px;font-size:21.5px;font-weight:800;line-height:25px;color:var(--white)}
.hero-text{position:absolute;left:79px;top:125px;width:300px;font-size:9px;line-height:13px;color:var(--white)}
.btn{position:absolute;width:131px;height:31px;background:var(--teal);color:var(--white);font-size:10px;font-weight:700;display:flex;align-items:center;justify-content:center;border-radius:1px}
.circle{position:absolute;border-radius:50%}
.h2{position:absolute;font-size:21px;font-weight:800;color:var(--pink)}
.body-text{position:absolute;font-size:9.4px;line-height:13.1px;color:var(--text)}
.services{position:absolute;left:79px;top:666px;width:580px;display:flex}
.service{width:145px}
.service-photo{height:145px}
.service-name{text-align:center;font-size:11px;font-weight:700;margin-top:8px;color:var(--text)}
.contact-photo{position:absolute;left:0;top:924px;width:738px;height:247px;
  background:linear-gradient(100deg,#c9a27a 0%,#e9e7ec 25%,#dfe2ea 50%,#8a7a70 70%,#c79a6a 85%,#3e3c44 100%)}
.footer-icons{position:absolute;left:79px;top:1182px;display:flex;gap:8px}
.footer-icons span{width:8px;height:8px;border-radius:2px;background:var(--pink)}
.footer-links{position:absolute;right:79px;top:1183px;display:flex;gap:15px;font-size:6.4px;font-weight:500;color:var(--pink);list-style:none}
</style>
</head>
<body>
<header>
  <div class="hero-photo" role="img" aria-label="Warm backlit photo of a woman raising her arms toward the sky outdoors"></div>
  <div class="brand"><span class="brand-dot"></span>Fjordlys og samhold</div>
  <ul class="nav-links"><li>ABOUT</li><li>SERVICES</li><li>BLOG</li><li>CONTACT</li></ul>
  <div class="hero-panel"></div>
  <h1 class="hero-title">The best way out<br>is always through</h1>
  <p class="hero-text">We focus on therapy, learning, mastery and growth for children and teenagers with special needs, within the family dynamics, or in a group setting.</p>
  <a class="btn" style="left:79px;top:197px">Learn More</a>
</header>

<section class="about">
  <div class="circle" style="left:192px;top:293px;width:122px;height:122px;background:var(--pink-soft)"></div>
  <div class="circle" role="img" aria-label="Photo of a person walking down a sunlit tree-lined country road" style="left:79px;top:310px;width:204px;height:204px;background:radial-gradient(circle at 25% 30%,#f2e2a0 0%,#9a8a4a 35%,#5a5a2e 65%,#3e3a22 100%)"></div>
  <div class="circle" style="left:41px;top:441px;width:100px;height:100px;background:var(--pink)"></div>
  <h2 class="h2" style="left:395px;top:343px">Who are we</h2>
  <p class="body-text" style="left:395px;top:380px;width:270px">Norwegian psychologist service: working with therapy, personal development, mastery and personal growth. Focus: children and teenagers with special needs; family dynamics; group processes; individuals with a need for therapy and personal growth.</p>
  <a class="btn" style="left:395px;top:457px">Learn More</a>
</section>

<section class="services-section">
  <h2 class="h2" style="left:79px;top:587px">Our Services</h2>
  <p class="body-text" style="left:79px;top:624px;width:600px">Lorem ipsum dolor sit amet, consectetur adipiscing elit. Donec vestibulum lorem massa, sed congue lorem scelerisque id. Aliquam scelerisque consectetur tristique. Integer metus nulla, dignissim sit amet bibendum id, bibendum non ex.</p>
  <div class="services">
    <div class="service"><div class="service-photo" role="img" aria-label="Photo of a smiling young woman in a hat and checked shirt outdoors" style="background:linear-gradient(160deg,#e0a04a,#7a4a2e 55%,#4a3a2a)"></div><div class="service-name">Investigation</div></div>
    <div class="service"><div class="service-photo" role="img" aria-label="Photo of two people in conversation at a table" style="background:linear-gradient(120deg,#a89a8c,#5a5048 50%,#c08a4a)"></div><div class="service-name">Consulting</div></div>
    <div class="service"><div class="service-photo" role="img" aria-label="Photo of a teacher working with children at a classroom table" style="background:linear-gradient(150deg,#e6eef2,#d8c2a8 50%,#8aa8b8)"></div><div class="service-name">Courses</div></div>
    <div class="service"><div class="service-photo" role="img" aria-label="Photo of a child with open arms by the sea" style="background:linear-gradient(180deg,#e8e0d8,#b8a898 55%,#5a4a40)"></div><div class="service-name">Therapy</div></div>
  </div>
  <a class="btn" style="left:304px;top:847px">Learn More</a>
</section>

<section class="contact">
  <div class="contact-photo" role="img" aria-label="Warm blurred photo of friends laughing together"></div>
  <h2 class="h2" style="left:79px;top:981px;color:var(--ink)">Contact Us</h2>
  <p class="body-text" style="left:79px;top:1017px;width:400px">Lorem ipsum dolor sit amet, consectetur adipiscing elit.<br>Donec vestibulum lorem massa, sed congue lorem scelerisque id.</p>
  <a class="btn" style="left:79px;top:1055px">Contact</a>
</section>

<footer>
  <div class="footer-icons"><span></span><span></span><span></span><span></span></div>
  <ul class="footer-links"><li>ABOUT</li><li>SERVICES</li><li>BLOG</li><li>CONTACT</li></ul>
</footer>
</body>
</html>
```